Financial & Tax Strategies

need to get a word press site with existing domains and condense existing content on existing site, make new site dynamic, need mobile too......need to take info from my brelva website and get modern, relevant site, less verbose on first page, way more things to click and engage people. Would like it to look like this , but with my color scheme and not quite as busy looking. I like much of the content on my tabs. Want maximize by seo capabilities on their as well. The number one thing I can say is to go to my existing website and get content, logo, etc there … www.pinebrookalderfirm.com .

Target Market(s)

Those 40 -65, business owners for at least 5 years. Higher net worth.

Number of Pages Required

5+ page

Font styles to use
Sans Serif

Colors
f04a50
e4daeb
ffffff

Requirements
Must have
• seo maximized, lots of places to click on to contact us, calls to action, relevant, conservative, want it to look like this and have the function as well.....slight variation on messaging, but like the simplicity on first view. https://www.delgartwhitbey.com/
Nice to have
• Some area along right side where videos we do will be.
Should not have
• feel too busy, but still have lots of opportunities to engage.

```html
<!DOCTYPE html>
<html lang="en">
<head>
<meta charset="utf-8">
<title>Pinebrook Alder Group</title>
<link href="https://fonts.googleapis.com/css2?family=Lato:wght@300;400;700;900&display=swap" rel="stylesheet">
<style>
:root{
  --red:#e8202a;
  --ink:#2b2b2b;
  --text:#555;
  --muted:#8a8a8a;
  --grey-band:#ececec;
  --page:#f4f4f4;
  --white:#ffffff;
  --footer:#2a2a2a;
  --footer-field:#444;
  --footer-bar:#ffffff;
  --line:#dcdcdc;
}
*{box-sizing:border-box;margin:0;padding:0}
html,body{width:1200px;height:3629px;overflow:hidden}
body{font-family:"Lato",Arial,sans-serif;color:var(--text);background:var(--page);position:relative}
.btn{display:inline-block;background:var(--red);color:var(--white);font-weight:700;font-size:14px;border-radius:22px;padding:0 28px;height:40px;line-height:40px;text-align:center}
.section-title{position:absolute;left:0;width:1200px;font-weight:400;color:var(--ink);text-align:center}

/* header */
.site-header{position:absolute;left:0;top:0;width:1200px;height:97px;background:var(--white)}
.menu-toggle{position:absolute;left:80px;top:38px;width:24px}
.menu-toggle span{display:block;height:2px;background:#333;margin-bottom:6px}
.brand{position:absolute;left:490px;top:24px;display:flex;align-items:center;gap:12px}
.brand-dot{width:44px;height:44px;border-radius:50%;background:#6a6a6a}
.brand-name{font-size:20px;line-height:22px;font-weight:700;color:#333}
.header-call{position:absolute;right:80px;top:30px;display:flex;align-items:center;gap:10px}
.phone-badge{width:32px;height:32px;border-radius:50%;background:var(--red);display:flex;align-items:center;justify-content:center}
.header-call p{font-size:13px;line-height:15px;color:#333}
.header-call p b{color:var(--red);font-weight:700}

/* hero */
.hero{position:absolute;left:0;top:97px;width:1200px;height:539px;background:linear-gradient(180deg,#b9c8cf 0%,#8aa0a8 22%,#5d7f52 45%,#4f7a3a 70%,#6c8e45 100%)}
.hero-arrow{position:absolute;top:250px;width:24px;height:40px}
.hero-caption{position:absolute;left:341px;top:198px;width:518px;height:220px;background:rgba(30,30,30,.62);text-align:center;padding-top:36px}
.hero-caption h1{font-size:34px;font-weight:400;color:var(--white)}
.hero-caption p{font-size:14px;line-height:18px;color:#ddd;margin:10px 70px 20px}
.hero-dots{position:absolute;left:578px;top:505px;display:flex;gap:8px}
.hero-dots i{width:9px;height:9px;border-radius:50%;background:rgba(255,255,255,.6)}
.hero-dots i.on{background:var(--white)}

/* about */
.about{position:absolute;left:0;top:636px;width:1200px;height:750px;background:var(--white)}
.about-title{top:70px;font-size:34px}
.divider{position:absolute;left:540px;top:118px;width:120px;height:20px}
.about-text{position:absolute;left:205px;top:150px;width:790px;font-size:14px;line-height:21px;text-align:center}
.about-btn{position:absolute;left:552px;top:260px;padding:0 22px}
.strategies-title{top:354px;font-size:33px}
.strategy-card{position:absolute;top:428px;width:242px;height:223px;border-radius:16px;background:var(--white);box-shadow:0 2px 14px rgba(0,0,0,.12);text-align:center;padding:0 22px}
.strategy-card svg{margin-top:50px}
.strategy-card p{font-size:15px;line-height:20px;color:#333;margin-top:18px}
.strategy-card.active{background:var(--red)}
.strategy-card.active p{color:var(--white)}

/* graphs */
.graphs{position:absolute;left:0;top:1386px;width:1200px;height:513px;background:var(--grey-band)}
.graphs h2{position:absolute;left:80px;top:98px;width:480px;font-size:32px;line-height:38px;font-weight:400;color:var(--ink)}
.graphs p{position:absolute;left:80px;top:212px;width:460px;font-size:13px;line-height:19px}
.graphs .btn{position:absolute;left:80px;top:334px;padding:0 26px}
.laptop{position:absolute;left:588px;top:66px;width:537px;height:387px}

/* blogs */
.blogs-title{top:1968px;font-size:33px}
.blog-card{position:absolute;top:2032px;width:343px;height:375px;background:var(--white);box-shadow:0 1px 8px rgba(0,0,0,.08);padding:12px}
.blog-media{width:100%;height:210px}
.blog-card h3{font-size:16px;font-weight:700;color:#222;margin:14px 0 8px}
.blog-card p{font-size:13px;line-height:18px}
.blog-card a{display:inline-block;font-size:12px;color:#444;margin-top:8px;border-bottom:1px solid #999}
.facts-btn{position:absolute;left:500px;top:2456px;width:200px}

/* testimonials */
.testimonials-title{top:2536px;font-size:33px}
.testimonial-list{position:absolute;left:0;top:2613px;width:1200px;display:flex;justify-content:center;gap:28px}
.testimonial{width:302px;height:338px;background:var(--white);border-radius:16px;box-shadow:0 2px 12px rgba(0,0,0,.1);text-align:center;padding:28px 24px}
.avatar{width:96px;height:96px;border-radius:50%;margin:0 auto;background:linear-gradient(180deg,#c9c9c9,#8c8c8c)}
.testimonial h4{font-size:16px;color:#222;font-weight:700;margin:18px 0 10px}
.testimonial p{font-size:13px;line-height:18px}
.t-dots{position:absolute;left:582px;top:2976px;display:flex;gap:6px}
.t-dots i{width:8px;height:8px;border-radius:50%;background:#f2a1a4}
.t-dots i.on{background:var(--red)}

/* quick contact */
.quick-email{position:absolute;left:304px;top:3052px;width:596px;height:42px;display:flex;gap:10px}
.quick-email span{flex:1;background:var(--white);border-radius:21px;font-size:13px;color:#777;line-height:42px;padding-left:22px}
.quick-email b{width:160px;height:42px;line-height:42px;background:var(--red);color:var(--white);border-radius:21px;text-align:center;font-size:14px}
.call-us{position:absolute;left:0;top:3132px;width:1200px;display:flex;justify-content:center;align-items:center;gap:14px;font-size:28px;font-weight:900;color:#222}
.call-us .phone-badge{width:52px;height:52px}

/* footer */
.site-footer{position:absolute;left:0;top:3246px;width:1200px;height:334px;background:var(--footer);color:#ddd}
.foot-brand{position:absolute;left:80px;top:60px;display:flex;align-items:center;gap:12px}
.foot-brand .brand-dot{background:#e6e6e6;width:40px;height:40px}
.foot-brand .brand-name{color:var(--white)}
.foot-about{position:absolute;left:80px;top:126px;width:260px;font-size:13px;line-height:20px;color:#ddd}
.foot-col{position:absolute;top:56px}
.foot-col h5{font-size:15px;font-weight:400;color:var(--white);padding-bottom:8px;border-bottom:2px solid var(--red);display:inline-block;margin-bottom:16px}
.link-list{list-style:none;font-size:13px;line-height:23px}
.link-list li::before{content:"•";margin-right:10px}
.addr-list{list-style:none}
.addr-list li{display:flex;align-items:flex-start;gap:10px;font-size:13px;line-height:21px;margin-bottom:6px}
.addr-list svg{margin-top:3px;flex:none}
.contact-form{display:grid;grid-template-columns:repeat(3,1fr);gap:6px;width:296px}
.field{height:28px;background:var(--footer-field);font-size:12px;line-height:28px;padding-left:8px;color:#eee}
.field.msg{grid-column:span 3;height:70px;line-height:20px;padding-top:4px}
.form-btn{grid-column:span 2;height:32px;line-height:32px;font-size:12px;padding:0;margin-top:8px;background:var(--red);color:var(--white);border-radius:16px}
.footer-bar{position:absolute;left:0;top:3580px;width:1200px;height:49px;background:var(--footer-bar)}
.footer-bar p{position:absolute;left:80px;top:17px;font-size:12px;color:#333}
.social{position:absolute;right:80px;top:12px;display:flex;gap:10px}
.social i{width:24px;height:24px;border-radius:50%;background:var(--red)}
.social i.dark{background:#222}
</style>
</head>
<body>

<header class="site-header">
  <div class="menu-toggle"><span></span><span></span><span></span></div>
  <div class="brand"><span class="brand-dot"></span><span class="brand-name">Pinebrook<br>Alder Group</span></div>
  <div class="header-call">
    <span class="phone-badge"><svg width="16" height="16" viewBox="0 0 24 24"><path fill="#fff" d="M6.6 10.8a15 15 0 0 0 6.6 6.6l2.2-2.2c.3-.3.7-.4 1-.2 1.1.4 2.3.6 3.6.6.6 0 1 .4 1 1V20c0 .6-.4 1-1 1A17 17 0 0 1 3 4c0-.6.4-1 1-1h3.5c.6 0 1 .4 1 1 0 1.3.2 2.5.6 3.6.1.3 0 .7-.2 1z"/></svg></span>
    <p><b>Call us Now</b><br>916.555.0142</p>
  </div>
</header>

<section class="hero" role="img" aria-label="Alpine valley landscape with green meadows, a lake and mountains">
  <svg class="hero-arrow" style="left:36px" viewBox="0 0 24 40"><path d="M18 4 6 20l12 16" stroke="#fff" stroke-width="3" fill="none"/></svg>
  <svg class="hero-arrow" style="right:36px" viewBox="0 0 24 40"><path d="M6 4l12 16L6 36" stroke="#fff" stroke-width="3" fill="none"/></svg>
  <div class="hero-caption">
    <h1>Financial Sensibility</h1>
    <p>Want predictable cash flow when you retire? We do what financial advisors &amp; accountants don't.</p>
    <span class="btn">Conservative Solutions</span>
  </div>
  <div class="hero-dots"><i></i><i class="on"></i><i></i><i></i></div>
</section>

<section class="about">
  <h2 class="section-title about-title">About us</h2>
  <svg class="divider" viewBox="0 0 120 20"><line x1="0" y1="10" x2="44" y2="10" stroke="#e8202a" stroke-width="2"/><circle cx="60" cy="10" r="7" fill="none" stroke="#999" stroke-width="2"/><line x1="76" y1="10" x2="120" y2="10" stroke="#e8202a" stroke-width="2"/></svg>
  <p class="about-text">As retirement inches closer, have you ever wondered if there were a company that could secure better returns than CD's, yet still be able to access your money inexpensively and as importantly, avoid the years it takes for your portfolio to recover from the big and routine crashes like in '87, '93, 2001 and 2008? What if Pinebrook Alder Group could provide this peace of mind AND not charge you those seemingly small (1-3%) portfolio devastating fees? Your financial advisor can never promise that you will get "X" per month on date "X".....why? We can answer that and we can guarantee both.</p>
  <span class="btn about-btn">Too good to be true? Try us</span>

  <h2 class="section-title strategies-title">Tax Strategies Accountants &amp; Financial Advisors Don't Have</h2>

  <div class="strategy-card active" style="left:80px">
    <svg width="44" height="44" viewBox="0 0 44 44" fill="none" stroke="#fff" stroke-width="2.5"><path d="M4 40h36"/><path d="M10 36V24M18 36V16M26 36V22M34 36V10"/><path d="M8 18l10-8 8 6 12-10"/></svg>
    <p>Insuring Portfolios Against Market Crashes</p>
  </div>
  <div class="strategy-card" style="left:346px">
    <svg width="44" height="44" viewBox="0 0 44 44" fill="none" stroke="#e8202a" stroke-width="2.5"><path d="M14 6v20h18"/><path d="M14 26l-6 10M32 26l4 10"/><path d="M6 38c10 4 24 4 34-2"/><path d="M14 12h10"/></svg>
    <p>Seemingly Small Fees Devastate Retirements We Don't Charge Them</p>
  </div>
  <div class="strategy-card" style="left:612px">
    <svg width="44" height="44" viewBox="0 0 44 44" fill="none" stroke="#e8202a" stroke-width="2.5"><rect x="8" y="4" width="28" height="36" rx="2"/><rect x="4" y="12" width="22" height="12" fill="#e8202a"/><path d="M14 32h16M14 36h12"/></svg>
    <p>Business Owners &amp; Executives Love Our Tax &amp; Bonus Strategies!</p>
  </div>
  <div class="strategy-card" style="left:878px">
    <svg width="44" height="44" viewBox="0 0 44 44" fill="none" stroke="#e8202a" stroke-width="2.5"><circle cx="22" cy="12" r="8"/><path d="M22 20v10M14 30h16l-3 10H17z"/></svg>
    <p>401k, Mutual Fund &amp; IRA Myths Revealed</p>
  </div>
</section>

<section class="graphs">
  <h2>Graphs can speak a thousand words</h2>
  <p>Ever wonder how much of your portfolio is the money you put into your 401k, IRA or Mutual Fund and how much those accounts have netted you over the last 10, 20, 30 years plus? Fees, crashes and financial advisors have not and will not educate you on this. We'll get you up to speed on your money and your financial future.</p>
  <span class="btn">Telling Graphs</span>

  <svg class="laptop" viewBox="0 0 537 387" role="img" aria-label="Line chart on a laptop screen comparing annual change in the market index with protected growth using a 0% floor">
    <rect x="36" y="0" width="465" height="352" rx="14" fill="#1e1e1e"/>
    <rect x="50" y="14" width="437" height="322" fill="#fff"/>
    <path d="M0 352h537l-14 22H14z" fill="#cfcfcf"/>
    <rect x="232" y="352" width="72" height="6" fill="#a8a8a8"/>
    <text x="268" y="30" font-size="9" font-weight="700" text-anchor="middle" fill="#222" font-family="Lato,sans-serif">Historical Comparison: Market Index vs. Risk Protection with a 0% Floor</text>
    <g stroke="#e0e0e0" stroke-width="1">
      <line x1="90" y1="50" x2="460" y2="50"/><line x1="90" y1="85" x2="460" y2="85"/><line x1="90" y1="120" x2="460" y2="120"/><line x1="90" y1="155" x2="460" y2="155"/><line x1="90" y1="190" x2="460" y2="190"/><line x1="90" y1="225" x2="460" y2="225"/><line x1="90" y1="260" x2="460" y2="260"/><line x1="90" y1="295" x2="460" y2="295"/>
    </g>
    <g font-size="8" fill="#333" font-family="Lato,sans-serif" text-anchor="end">
      <text x="86" y="53">120.00%</text><text x="86" y="88">80.00%</text><text x="86" y="123">40.00%</text><text x="86" y="158">0.00%</text><text x="86" y="193">-40.00%</text><text x="86" y="228">-80.00%</text><text x="86" y="263">-120.00%</text>
    </g>
    <g font-size="8" fill="#333" font-family="Lato,sans-serif" text-anchor="middle">
      <text x="100" y="308">00</text><text x="136" y="308">01</text><text x="172" y="308">02</text><text x="208" y="308">03</text><text x="244" y="308">04</text><text x="280" y="308">05</text><text x="316" y="308">06</text><text x="352" y="308">07</text><text x="388" y="308">08</text><text x="424" y="308">09</text><text x="452" y="308">10</text>
    </g>
    <polyline points="100,155 136,155 172,155 208,140 244,128 280,122 316,108 352,100 388,100 424,90 452,70" fill="none" stroke="#2a6fc0" stroke-width="2.5"/>
    <polyline points="100,155 136,166 172,185 208,196 244,186 280,180 316,176 352,170 388,200 424,180 452,175" fill="none" stroke="#c0262b" stroke-width="2.5"/>
    <g fill="#2a6fc0"><circle cx="100" cy="155" r="3"/><circle cx="208" cy="140" r="3"/><circle cx="316" cy="108" r="3"/><circle cx="424" cy="90" r="3"/><circle cx="452" cy="70" r="3"/></g>
    <g fill="#c0262b"><circle cx="136" cy="166" r="3"/><circle cx="208" cy="196" r="3"/><circle cx="316" cy="176" r="3"/><circle cx="388" cy="200" r="3"/><circle cx="452" cy="175" r="3"/></g>
    <circle cx="150" cy="325" r="4" fill="#c0262b"/><text x="158" y="328" font-size="8" fill="#333" font-family="Lato,sans-serif">Annual Change in Market Index</text>
    <circle cx="290" cy="325" r="4" fill="#2a6fc0"/><text x="298" y="328" font-size="8" fill="#333" font-family="Lato,sans-serif">Annual Change with Growth Cap and Floor</text>
  </svg>
</section>

<h2 class="section-title blogs-title">Blogs, Videos &amp; Radio</h2>
<article class="blog-card" style="left:68px">
  <div class="blog-media" role="img" aria-label="Businessman celebrating under falling banknotes" style="background:linear-gradient(160deg,#d8d8d8,#9a9a9a)"></div>
  <h3>Money Blog</h3>
  <p>Lorem Ipsum is simply dummy the printing and typesetting industry. Lorem Ipsum has been the in the standard dummy.</p>
  <a>Continue..</a>
</article>
<article class="blog-card" style="left:431px">
  <div class="blog-media" role="img" aria-label="Portrait of a smiling advisor in a suit" style="background:linear-gradient(160deg,#c9ccd2,#7c8794)"></div>
  <h3>PAG Videos</h3>
  <p>Lorem Ipsum is simply dummy the printing and typesetting industry. Lorem Ipsum has been the in the standard dummy.</p>
  <a>Continue..</a>
</article>
<article class="blog-card" style="left:794px">
  <div class="blog-media" style="background:#f5f5f5;display:flex;align-items:center;justify-content:center;gap:12px">
    <span style="width:40px;height:40px;border-radius:50%;background:var(--red)"></span>
    <span style="font-size:34px;font-weight:900;color:#222">StreamWave</span>
  </div>
  <h3>StreamWave Radio</h3>
  <p>Catch us on StreamWave Radio's Lena Marsh Show KRVT Talk 710 am<br>(Money Making Max &amp; Regular Ray)</p>
  <a>Continue..</a>
</article>
<span class="btn facts-btn">401k Facts</span>

<h2 class="section-title testimonials-title">Testimonials</h2>
<div class="testimonial-list">
  <article class="testimonial">
    <div class="avatar" role="img" aria-label="Client portrait"></div>
    <h4>Dale Morrow</h4>
    <p>National Business Alliance Turnaround CEO of the Year. I'm a CFO by trade. PAG has strategies for families, executive &amp; business owners that accountants and financial advisors don't have. Highest recommendation</p>
  </article>
  <article class="testimonial">
    <div class="avatar" role="img" aria-label="Client portrait"></div>
    <h4>Ray Ellison</h4>
    <p>Probate Attorney. As an attorney, my job is to weigh risk. As an investor, weighing risk and reward is even more important. As someone retiring in next 15 years, I wanted to eliminate the risks of a stock market crash. PAG does this better than any other company.</p>
  </article>
  <article class="testimonial">
    <div class="avatar" role="img" aria-label="Client portrait"></div>
    <h4>Neil Hartman</h4>
    <p>Doctor. Being a doctor requires attention to detail. Pinebrook Alder Group helped navigate and educate me on exactly how to decipher my portfolio statement. I would have changed 10 years ago if I would have known what I know now about money. Call them; you'll be happy you did</p>
  </article>
</div>
<div class="t-dots"><i class="on"></i><i></i><i></i></div>

<div class="quick-email"><span>Shoot us a quick email here</span><b>Submit</b></div>
<div class="call-us">CALL US
  <span class="phone-badge"><svg width="26" height="26" viewBox="0 0 24 24"><path fill="#fff" d="M6.6 10.8a15 15 0 0 0 6.6 6.6l2.2-2.2c.3-.3.7-.4 1-.2 1.1.4 2.3.6 3.6.6.6 0 1 .4 1 1V20c0 .6-.4 1-1 1A17 17 0 0 1 3 4c0-.6.4-1 1-1h3.5c.6 0 1 .4 1 1 0 1.3.2 2.5.6 3.6.1.3 0 .7-.2 1z"/></svg></span>
  916.555.0142</div>

<footer class="site-footer">
  <div class="foot-brand"><span class="brand-dot"></span><span class="brand-name">Pinebrook<br>Alder Group</span></div>
  <p class="foot-about">Pinebrook Alder Group Bringing sensibility, predictability and peace of mind in retirement. We will do things for your financial lives accountants and financial advisors won't and can't.</p>
  <div class="foot-col" style="left:406px">
    <h5>Quick Link</h5>
    <ul class="link-list"><li>Home</li><li>About us</li><li>Services</li><li>Blogs</li><li>Testimonials</li><li>Contact us</li></ul>
  </div>
  <div class="foot-col" style="left:573px">
    <h5>Address</h5>
    <ul class="addr-list">
      <li><svg width="12" height="16" viewBox="0 0 12 16"><path d="M6 0a6 6 0 0 0-6 6c0 4.5 6 10 6 10s6-5.5 6-10a6 6 0 0 0-6-6zm0 8.5A2.5 2.5 0 1 1 6 3.5a2.5 2.5 0 0 1 0 5z" fill="#ddd"/></svg><span>4821 Larkfield Road,<br>Cedar Vale,<br>CA 95000</span></li>
      <li><svg width="14" height="14" viewBox="0 0 24 24"><path fill="#ddd" d="M6.6 10.8a15 15 0 0 0 6.6 6.6l2.2-2.2c.3-.3.7-.4 1-.2 1.1.4 2.3.6 3.6.6.6 0 1 .4 1 1V20c0 .6-.4 1-1 1A17 17 0 0 1 3 4c0-.6.4-1 1-1h3.5c.6 0 1 .4 1 1 0 1.3.2 2.5.6 3.6.1.3 0 .7-.2 1z"/></svg><span>916.555.0142</span></li>
      <li><svg width="14" height="12" viewBox="0 0 14 12"><rect x="1" y="1" width="12" height="10" fill="none" stroke="#ddd" stroke-width="1.5"/><path d="M1 1l6 5 6-5" fill="none" stroke="#ddd" stroke-width="1.5"/></svg><span>Sales@PinebrookAlder.com</span></li>
    </ul>
  </div>
  <div class="foot-col" style="left:827px">
    <h5>Contact us</h5>
    <div class="contact-form">
      <span class="field">Name</span><span class="field">Email</span><span class="field">Phone</span>
      <span class="field msg">Message</span>
      <span class="form-btn btn">Baby Boomer Edition</span>
    </div>
  </div>
</footer>
<div class="footer-bar">
  <p>CopyRight © 2019 Pinebrook Alder Group. All Right Reserve</p>
  <div class="social"><i></i><i></i><i></i><i class="dark"></i><i class="dark"></i></div>
</div>

</body>
</html>
```